Bref créative
Stationary - Morvane Advisory
Business Card, Letterhead & Pen Design
Professional
Helmut Draven
Director
Address line 1
Address line 2
Address line 3
Address line 4
Post Code
QRP@QRP.example
For the business card I like the idea of front/back designs, where either there is something which joins the front and back or there is a slightly modified logo on the back... You're call, I'm open to anything here, so if you come up with something just try it out, I'll give everyone feedback where possible!
Please don't just stick my logo on a pen and say "hey, here you go...", for the pen design I'm looking for colours etc and where they are placed on the pen too!
Anything you think would look good!
Image file to show the logo
Extra images (inc psds!) for the logo

```html
<!DOCTYPE html>
<html lang="en">
<head>
<meta charset="utf-8">
<title>Morvane Advisory – Business Card</title>
<link href="https://fonts.googleapis.com/css2?family=Exo+2:wght@600&family=Arimo:wght@400;700&display=swap" rel="stylesheet">
<style>
  :root {
    --backdrop: #2b2b2d;
    --card: #ffffff;
    --teal: #1a8fb0;
    --teal-dark: #0f6f8c;
    --teal-light: #5cc0dc;
    --ice: #e6f3f8;
    --ink: #1e1e1e;
    --tab-top: #f4f4f4;
    --tab-bottom: #d4d6d8;
  }
  html, body {
    margin: 0;
    width: 1200px;
    height: 780px;
    overflow: hidden;
    background: var(--backdrop);
  }
  .card {
    position: absolute;
    left: 60px;
    top: 80px;
    width: 1080px;
    height: 620px;
    background: var(--card);
    border-radius: 34px;
    overflow: hidden;
    box-shadow: 0 10px 30px rgba(0,0,0,.45);
  }
  .side-band {
    position: absolute;
    left: 95px;
    top: 0;
    width: 92px;
    height: 100%;
    background: linear-gradient(90deg, var(--teal-dark), var(--teal) 45%, var(--teal-light));
  }
  .side-rule {
    position: absolute;
    top: 0;
    height: 100%;
    background: var(--teal);
  }
  .side-rule.one { left: 196px; width: 4px; opacity: .7; }
  .side-rule.two { left: 206px; width: 2px; opacity: .45; }
  .brand {
    position: absolute;
    left: 112px;
    top: 92px;
    display: flex;
    align-items: center;
    gap: 22px;
  }
  .brand-square {
    width: 60px;
    height: 60px;
    background: var(--teal-dark);
  }
  .brand-name {
    font-family: "Exo 2", sans-serif;
    font-weight: 600;
    font-size: 60px;
    color: var(--teal);
    letter-spacing: 1px;
    line-height: 1;
    white-space: nowrap;
  }
  .address {
    position: absolute;
    left: 440px;
    top: 360px;
    margin: 0;
    font-family: "Arimo", sans-serif;
    font-size: 19px;
    line-height: 28px;
    color: var(--ink);
    white-space: nowrap;
  }
  .contacts {
    position: absolute;
    left: 440px;
    top: 444px;
    margin: 0;
    padding: 0;
    list-style: none;
    font-family: "Arimo", sans-serif;
    font-size: 19px;
    color: var(--ink);
  }
  .contacts li {
    display: flex;
    align-items: center;
    gap: 12px;
    height: 34px;
    white-space: nowrap;
  }
  .contacts svg { width: 20px; height: 20px; flex: none; }
  .identity-panel {
    position: absolute;
    left: 730px;
    top: 265px;
    width: 260px;
    height: 250px;
    border-radius: 26px;
    background: var(--ice);
  }
  .person {
    position: absolute;
    left: 730px;
    top: 400px;
    width: 260px;
    text-align: center;
  }
  .person-name {
    font-family: "Arimo", sans-serif;
    font-weight: 700;
    font-size: 27px;
    color: var(--teal);
    margin: 0 0 8px;
    white-space: nowrap;
  }
  .person-role {
    display: inline-block;
    padding: 6px 24px;
    font-family: "Arimo", sans-serif;
    font-size: 17px;
    color: var(--ink);
    background: linear-gradient(var(--tab-top), var(--tab-bottom));
    border-radius: 4px;
  }
</style>
</head>
<body>
  <main class="card">
    <div class="side-band"></div>
    <div class="side-rule one"></div>
    <div class="side-rule two"></div>

    <header class="brand">
      <div class="brand-square"></div>
      <span class="brand-name">Morvane Advisory</span>
    </header>

    <p class="address">Suite 48 Harrow Lane,<br>Eastvale, Zip 7701,Country</p>

    <ul class="contacts">
      <li>
        <svg viewBox="0 0 20 20" aria-hidden="true"><path d="M5 2 L8 6 L6.5 8 Q8.5 12 12 13.5 L14 12 L18 15 L16 18 Q8 18 3 10 Q2 5 5 2 Z" fill="var(--teal)"/></svg>
        <span>07000 482 915</span>
      </li>
      <li>
        <svg viewBox="0 0 20 20" aria-hidden="true"><circle cx="10" cy="10" r="4" fill="none" stroke="var(--ink)" stroke-width="2"/><path d="M14 7 V12 Q14 15 17 14 Q19 10 17 6 Q13 1 7 3 Q2 6 3 12 Q5 18 13 17" fill="none" stroke="var(--ink)" stroke-width="2"/></svg>
        <span>QRP@QRP.example</span>
      </li>
      <li>
        <svg viewBox="0 0 20 20" aria-hidden="true"><circle cx="10" cy="10" r="8" fill="var(--teal-light)"/><path d="M2 10 H18 M10 2 Q5 10 10 18 Q15 10 10 2" fill="none" stroke="#fff" stroke-width="1.2"/></svg>
        <span>www.QRP.example</span>
      </li>
    </ul>

    <div class="identity-panel"></div>
    <div class="person">
      <p class="person-name">Helmut Draven</p>
      <span class="person-role">Director</span>
    </div>
  </main>
</body>
</html>
```